Business Stationary & Card Design

Double sided business cards, letterhead, horizontal brochure, and envelope design using our logo. We want a modern minimal look. One side of the business card should be only our logo and maybe our slogan "Get It Done Right". The other side should include our coil spring and not the logo again. Watermark like (or not) positioned partially, horizontal, on angle, or a combination of. IF a background color or accent color is used we like blue (4885ed). The letterhead, brochure, and envelope design should be similar to the card. Except no solid background color.Maybe the spring at the bottom of the letterhead page watermark style and partial. Additional info on the business card should be present:
Employee Name
Position
Phone
Email
Address
The final design should communicate strength, simplicity, and newness.

Target Market(s)

35-55 Male & Female

Industry/Entity Type

Automotive

Contact Information for Business Card

One side of the double sided business card should be only our logo and maybe our slogan "Get It Done Right". The other side should include our coil spring and not the logo again. Watermark like (or not) positioned partially, horizontal, on angle, or a combination of. IF a background color or accent color is used we like blue (4885ed). Additional info on the business card should be present:
Employee Name
Position
Phone
Email
Address

Font styles to use
Other font styles liked:
• Use font that compliments the attached font. Maybe plain eurostyle?

Colors
0492cd
3276b5

Requirements
Must have
• Use the coil spring in a subtle unique way (s). Double sided business card
Should not have
• Clutter, colors that do not coordinate well with our logo. Fonts that do not compliment our font.

```html
<!DOCTYPE html>
<html lang="en">
<head>
<meta charset="utf-8">
<title>Torque Line — Stationery Set</title>
<link href="https://fonts.googleapis.com/css2?family=Michroma&display=swap" rel="stylesheet">
<style>
  :root {
    --backdrop: #7e7f81;
    --brand-yellow: #e0be22;
    --ink: #000000;
    --paper: #ffffff;
  }
  * { margin: 0; padding: 0; box-sizing: border-box; }
  html, body { width: 1200px; height: 1200px; overflow: hidden; }
  body {
    position: relative;
    background: var(--backdrop);
    font-family: "Michroma", sans-serif;
    color: var(--ink);
  }
  .piece { position: absolute; }
  .wordmark {
    position: absolute;
    font-family: "Michroma", sans-serif;
    font-weight: 400;
    letter-spacing: 0.04em;
    white-space: nowrap;
    line-height: 1;
  }
  .flap { position: absolute; left: 0; top: 0; display: block; }
  .flap-mark {
    color: var(--brand-yellow);
    font-size: 13px;
    transform: translate(-50%, -50%) rotate(180deg);
  }

  /* Large envelope */
  .envelope-large { left: 107px; top: 66px; width: 473px; height: 746px; }
  .envelope-large .body {
    position: absolute; left: 0; top: 78px; width: 473px; height: 668px;
    background: var(--brand-yellow);
    overflow: hidden;
  }
  .envelope-large .flap-mark { left: 237px; top: 38px; }
  .envelope-large .side-mark {
    color: var(--paper);
    font-size: 20px;
    left: 65px; top: 517px;
    transform: translate(-50%, -50%) rotate(-90deg);
  }
  .envelope-large .contact-vertical {
    position: absolute;
    left: 414px; top: 165px;
    font-size: 9.5px;
    line-height: 14.5px;
    transform: translate(-50%, -50%) rotate(-90deg);
    white-space: nowrap;
  }

  /* Small envelope */
  .envelope-small { left: 106px; top: 846px; width: 474px; height: 288px; }
  .envelope-small .body {
    position: absolute; left: 0; top: 71px; width: 474px; height: 217px;
    background: var(--brand-yellow);
    overflow: hidden;
  }
  .envelope-small .flap-mark { left: 238px; top: 38px; }
  .envelope-small .corner-mark {
    color: var(--paper); font-size: 13px; left: 30px; top: 28px;
  }
  .envelope-small .contact {
    position: absolute; left: 247px; top: 157px;
    font-size: 8.5px; line-height: 12px; white-space: nowrap;
  }

  /* Business card front */
  .card-front {
    left: 705px; top: 78px; width: 341px; height: 194px;
    background: var(--brand-yellow);
  }
  .card-front .card-mark { color: var(--paper); font-size: 13px; left: 24px; top: 24px; }
  .card-front .slogan {
    position: absolute; right: 25px; top: 158px;
    font-size: 8px; letter-spacing: 0.02em; white-space: nowrap;
  }

  /* Business card back */
  .card-back {
    left: 705px; top: 284px; width: 341px; height: 194px;
    background: var(--brand-yellow);
    padding: 7px;
  }
  .card-back .face {
    width: 100%; height: 100%; background: var(--paper);
    text-align: center; padding-top: 47px;
  }
  .card-back .name { font-size: 18px; line-height: 1; letter-spacing: 0.02em; }
  .card-back .name .given { color: var(--brand-yellow); }
  .card-back .role { font-size: 8.5px; margin-top: 6px; }
  .card-back .details { font-size: 8.5px; line-height: 12.5px; margin-top: 13px; }
  .card-back .details .phone { margin-bottom: 3px; }

  /* Letterhead */
  .letterhead {
    left: 652px; top: 502px; width: 441px; height: 624px;
    background: var(--paper);
  }
  .letterhead .head-mark {
    color: var(--brand-yellow); font-size: 15px;
    left: 50%; top: 42px; transform: translateX(-50%);
  }
  .letterhead .footer-rule {
    position: absolute; left: 25px; right: 25px; top: 573px;
    border-top: 1px solid var(--brand-yellow);
  }
  .letterhead .footer {
    position: absolute; left: 0; right: 0; top: 581px;
    text-align: center; font-size: 8.5px; line-height: 15px;
  }
  .letterhead .footer span + span { margin-left: 12px; }
</style>
</head>
<body>

  <section class="piece envelope-large" aria-label="Large envelope">
    <svg class="flap" width="473" height="78" viewBox="0 0 473 78" aria-hidden="true">
      <path d="M0 78 L16 12 Q19 0 32 0 L441 0 Q454 0 457 12 L473 78 Z" fill="#000"/>
    </svg>
    <span class="wordmark flap-mark">TORQUE LINE</span>
    <div class="body">
      <span class="wordmark side-mark">TORQUE LINE</span>
      <div class="contact-vertical">
        <div>000.000.000</div>
        <div>INFO@TORQUELINE.COM</div>
        <div>STREET ADDRESS HERE, USA, 2476</div>
      </div>
    </div>
  </section>

  <section class="piece envelope-small" aria-label="Small envelope">
    <svg class="flap" width="474" height="71" viewBox="0 0 474 71" aria-hidden="true">
      <path d="M0 71 L16 12 Q19 0 32 0 L442 0 Q455 0 458 12 L474 71 Z" fill="#000"/>
    </svg>
    <span class="wordmark flap-mark">TORQUE LINE</span>
    <div class="body">
      <span class="wordmark corner-mark">TORQUE LINE</span>
      <div class="contact">
        <div>000.000.000</div>
        <div>INFO@TORQUELINE.COM</div>
        <div>STREET ADDRESS HERE, USA, 2476</div>
      </div>
    </div>
  </section>

  <section class="piece card-front" aria-label="Business card front">
    <span class="wordmark card-mark">TORQUE LINE</span>
    <p class="slogan">GET IT DONE RIGHT</p>
  </section>

  <section class="piece card-back" aria-label="Business card back">
    <div class="face">
      <p class="name"><span class="given">JOHN</span> SMITH</p>
      <p class="role">MARKETING MANAGER</p>
      <div class="details">
        <p class="phone">000.000.000</p>
        <p>INFO@TORQUELINE.COM</p>
        <p>STREET ADDRESS HERE,<br>USA, 2476</p>
      </div>
    </div>
  </section>

  <section class="piece letterhead" aria-label="Letterhead">
    <span class="wordmark head-mark">TORQUE LINE</span>
    <div class="footer-rule"></div>
    <div class="footer">
      <p><span>000.000.000</span><span>INFO@TORQUELINE.COM</span></p>
      <p>STREET ADDRESS HERE, USA, 2476</p>
    </div>
  </section>

</body>
</html>
```